High Tech Real Estate Startup needs a business card

We are developing an innovative real estate marketing product based around advanced search and virtual reality.

We talk to people, we need business cards.

Target Market(s)

The target market is technology professionals and realtors.

Contact Information for Business Card

The information to be included will include

Name
Title
Phone Number
E-mail Address
www.quelzo.com

It should use simple iconography for each one of those fields.

Font styles to use
Other font styles liked:
• Co, Jubilat, Avenir

Colors

Designer to choose colors to be used in the design.

Requirements
Must have
• Clean aesthetic,
• Good use of negative space.
• It should use our company logo, shown in the attached file. It is able to use the negative of that logo (coloured font and white background) and I have attached other acceptable accent colours in a swatch file.
Should not have
• Should not be too busy
• No extraneous text (slogans, tag lines etc)

```html
<!DOCTYPE html>
<html lang="en">
<head>
<meta charset="utf-8">
<title>Quelzo Business Card</title>
<link rel="stylesheet" href="https://fonts.googleapis.com/css2?family=Nunito+Sans:wght@400;600&display=swap">
<style>
  :root {
    --backdrop: #d6d6d4;
    --card: #ffffff;
    --brand-teal: #12bcc4;
    --ink: #5b6b72;
    --rule: #6e7c82;
  }
  * { margin: 0; padding: 0; box-sizing: border-box; }
  html, body {
    width: 1200px;
    height: 1000px;
    overflow: hidden;
    background: var(--backdrop);
    font-family: "Nunito Sans", "Avenir", sans-serif;
  }
  .canvas { position: relative; width: 1200px; height: 1000px; }
  .card {
    position: absolute;
    background: var(--card);
    border-radius: 40px;
  }
  .card--front { left: 152px; top: 102px; width: 626px; height: 358px; }
  .card--back  { left: 371px; top: 547px; width: 636px; height: 361px; }

  .wordmark {
    position: absolute;
    color: var(--brand-teal);
    font-weight: 600;
    line-height: 1;
    white-space: nowrap;
  }
  .card--front .wordmark {
    left: 0; right: 0; top: 128px;
    text-align: center;
    font-size: 96px;
    letter-spacing: 3px;
  }
  .card--back .wordmark {
    right: 46px; top: 274px;
    font-size: 42px;
    letter-spacing: 1px;
  }

  .person-name {
    position: absolute; left: 34px; top: 120px;
    font-size: 31px; font-weight: 400; color: var(--ink);
  }
  .person-title {
    position: absolute; left: 34px; top: 163px;
    font-size: 18px; font-weight: 400; color: var(--ink);
  }
  .title-rule {
    position: absolute; left: 189px; top: 177px;
    width: 413px; height: 2px; background: var(--rule);
  }

  .contact-list { position: absolute; left: 36px; top: 230px; list-style: none; }
  .contact-item {
    display: flex; align-items: center;
    height: 29px;
    font-size: 21px; letter-spacing: 2px; color: var(--ink);
  }
  .contact-icon { width: 18px; height: 18px; margin-right: 22px; fill: var(--ink); }
</style>
</head>
<body>
<main class="canvas">
  <section class="card card--front">
    <div class="wordmark">QUELZO</div>
  </section>

  <section class="card card--back">
    <h1 class="person-name">Name of Person</h1>
    <p class="person-title">Title of Person</p>
    <div class="title-rule"></div>

    <ul class="contact-list">
      <li class="contact-item">
        <svg class="contact-icon" viewBox="0 0 24 24" aria-hidden="true">
          <path d="M6.6 10.8a15 15 0 0 0 6.6 6.6l2.2-2.2c.3-.3.7-.4 1-.2 1.1.4 2.3.6 3.6.6.6 0 1 .4 1 1V20c0 .6-.4 1-1 1A17 17 0 0 1 3 4c0-.6.4-1 1-1h3.5c.6 0 1 .4 1 1 0 1.3.2 2.5.6 3.6.1.3 0 .7-.2 1z"/>
        </svg>
        <span>+123 456 7890</span>
      </li>
      <li class="contact-item">
        <svg class="contact-icon" viewBox="0 0 24 24" aria-hidden="true" fill="none" stroke="#5b6b72" stroke-width="2">
          <circle cx="12" cy="12" r="9"/>
          <ellipse cx="12" cy="12" rx="4" ry="9"/>
          <line x1="3" y1="12" x2="21" y2="12"/>
        </svg>
        <span>www.quelzo.com</span>
      </li>
      <li class="contact-item">
        <svg class="contact-icon" viewBox="0 0 24 24" aria-hidden="true">
          <path d="M3 5h18v14H3z M3 6l9 7 9-7" fill="var(--ink)" stroke="#ffffff" stroke-width="1.5"/>
        </svg>
        <span>E-mail Address</span>
      </li>
    </ul>

    <div class="wordmark">QUELZO</div>
  </section>
</main>
</body>
</html>
```